Design a cool print brochure for an NGO / Give your work a global impact!!

Hi,
I provide a full design brief (below, please scroll) and a mood board (attached) to help you visualize inside my head.. ;-)
I am also available to help and have worked many years in advertising; we will understand each other.
Objective:
To design an A4 folded in two presentation brochure for a non-profit consulting agency called Mer-ova.
Mer-ova works in sustainability and international development = working with NGO’s, governments and private sector on global issues such as global warming, education for all etc.
Strategy:
This document is a first step in developing a communication strategy. It will be distributed during a major international event called the Brenvik Outreach Forum.
Objective:
The double objective of the brochure is:
a) to inform the recipient of what Mer-ova is, in the shortest time possible.
b) to showcase relevant projects to demonstrate Mer-ova experience and expertise.
Target:
Main target:
Existing Mer-ova contacts, such as members of development organizations, NGOs, private sector foundations (CSR), regional networks and other development actors.
NB: the main target already has a certain awareness of Mer-ova: we will try to minimize text to maximize visual impact and readability.
Secondary target:
Mer-ova will also distribute the brochure to new prospects of interest during the Brenvik Forum.
Timing:
We will need to finalize the design and have the files by June 1st to allow time for print before the event.
Content:
The document should be concise, highly readable (no clutter) and include:
1. text (that we will provide)
and
2. visual elements such as images, shapes and info-graphics (that is you).
NB: Mer-ova does not have its own image bank; photos will be provided by you.
Format:
A4 folded in half - 4pp A5 - PORTRAIT FORMAT) with an impactful visual in the front, logo, title and headline (please see examples in the mood board attached).
Design elements:
Mer-ova does not have yet a visual identity (please see: http://mer-ova.org) so there is room for creativity and no graphic chart to follow.
The sector of consulting in international development is rather conservative but our intention is to be disruptive and create a “Wow” effect. We count on you for that!
Therefore, the design should be “structured”, “organized”, “uncluttered” but also “modern”, “impactful”, “highly visual” (think infographic or mind map to describe our services and projects).
Please, take the time to see the attached presentation: I give you guidelines and examples of what we want and what we like.
We are looking forward to seeing your work and I am available for comments, questions and support.
Thank you.
RM
Target Market(s)
The full brief is in the project description: please, scroll through it.
The target market is : our existing clients base, working in sustainable development (read: NGO and Concord Assembly people)
Industry/Entity Type
Ngo
Requirements
Must have
- - Design and color elements: please, no black and white. Our company website is in black and white and without graphics; we want the brochure to break away from that and start creating our brand identity; so please, show us colors and desing elements (shapes, backgrounds, etc).
- You have a chance to showcase your talent in terms of visual identity: what lines, forms, layout and colors can you come up with and apply throughout the brochure and serve as the visual identity of Mer-ova?
- The structure of the document should be:
- - Front cover: design elements + impacful photo (see mood board example attached) +our logo + this headline: "Collective action for sustainable development and impact"
- - Inside front: a graphic representation of "Our Services": such as core activity in the center circle and satellite circles for the services we offer.
- - Inside back:
- 1. Icons and text boxes for "Our projects"
- 2. A world map of the countries where we have worked. Full list of countries is here:
- http://mer-ova.org/experience-1
- - Back cover: our contact + logos of partners.
- Our partners are listed here:
- Please use their original logos (ie, in color).
- The design we will select will serve as a basis for a graphic chart...so more work to come...word to the wise ;)
- Please check out our website mer-ova.org to see what we do etc.
Nice to have
- Icons to reflect our services: what icons can you come up with to describe "training services", "building networks" or "program management"?
- I give examples in the mood board.
Should not have
- We are open to creativity and want to generate a "Wow" effect.
- Just note that the sector is rather conservative so flashy colors and cartoon like characters should be avoided. Think "earth, global change, Concord Assembly, climate" without going too green (it's overdone). ;-)
- Make us stand out in the NGO world
- Now you.

```html
<!DOCTYPE html>
<html lang="en">
<head>
<meta charset="utf-8">
<title>Mer-ova at a glance</title>
<link href="https://fonts.googleapis.com/css2?family=Montserrat:wght@400;700&family=Noto+Serif:wght@400&display=swap" rel="stylesheet">
<style>
  :root {
    --paper: #dfe4bf;
    --paper-light: #eef0d6;
    --olive: #8f8b55;
    --olive-dark: #7d7a48;
    --lime: #c5dc2a;
    --green: #8cc63f;
    --map-green: #9cc83d;
    --map-teal: #21b3a6;
    --map-tan: #c6b98a;
    --map-gold: #bfa345;
    --map-orange: #f07f4e;
    --orange: #e86d2a;
    --orange-light: #f58a4e;
    --amber: #e9b321;
    --teal-dark: #15a78f;
    --teal: #22b9a4;
    --teal-light: #84cfc6;
    --teal-soft: #5fc2b5;
    --ink: #5a5536;
    --ink-body: #5b5a45;
    --white: #ffffff;
  }
  html, body { margin: 0; padding: 0; overflow: hidden; }
  body { width: 1200px; height: 848px; background: var(--paper); }
  .spread {
    position: relative; width: 1200px; height: 848px; overflow: hidden;
    background: radial-gradient(ellipse at 30% 60%, var(--paper-light), var(--paper) 70%);
    font-family: "Montserrat", sans-serif;
  }
  .decor { position: absolute; inset: 0; }
  .display {
    position: absolute; margin: 0; color: var(--white);
    font-family: "Noto Serif", serif; font-weight: 400; line-height: 0.92;
  }
  .display .big { display: block; font-size: 58px; }
  .display .small { display: block; font-size: 36px; }
  .glance-title { left: 58px; top: 24px; }
  .presence-title { right: 47px; top: 24px; text-align: right; }
  .projects-title { left: 685px; top: 560px; }
  .projects-title .big { font-size: 44px; }
  .projects-title .small { font-size: 33px; }
  .service-label {
    position: absolute; margin: 0; color: var(--ink);
    font-size: 10.5px; font-weight: 700; line-height: 1.25; text-transform: uppercase;
  }
  .service-label.right { text-align: right; }
  .service-label.center { text-align: center; }
  .core-label {
    position: absolute; left: 226px; top: 466px; width: 160px; margin: 0;
    text-align: center; color: var(--ink);
    font-size: 12.5px; font-weight: 700; line-height: 1.32; text-transform: uppercase;
  }
  .map {
    position: absolute; left: 614px; top: 112px; width: 586px; height: 362px;
    border-radius: 28px;
    background: linear-gradient(100deg,
      var(--map-green) 0%, var(--map-green) 32%,
      var(--map-teal) 44%, var(--map-teal) 52%,
      var(--map-tan) 60%, var(--map-gold) 80%, var(--map-tan) 100%);
    opacity: .85;
  }
  .project-text {
    position: absolute; margin: 0; color: var(--ink-body);
    font-size: 11.5px; font-weight: 400; line-height: 1.35;
  }
</style>
</head>
<body>
<main class="spread">
  <svg class="decor" width="1200" height="848" viewBox="0 0 1200 848" aria-hidden="true">
    <defs>
      <radialGradient id="core-fill" cx="0.35" cy="0.3" r="0.8">
        <stop offset="0" stop-color="#ecea2a"/>
        <stop offset="0.5" stop-color="#d6e02a"/>
        <stop offset="0.8" stop-color="#8cc63f"/>
        <stop offset="1" stop-color="#e8b070"/>
      </radialGradient>
      <radialGradient id="sun" cx="1" cy="0" r="1">
        <stop offset="0" stop-color="#e08a2a"/>
        <stop offset="0.6" stop-color="#eab425"/>
        <stop offset="1" stop-color="#eab425" stop-opacity="0"/>
      </radialGradient>
    </defs>
    <circle cx="110" cy="40" r="210" fill="var(--olive)" opacity=".85"/>
    <g fill="none" stroke="var(--olive-dark)" opacity=".55">
      <circle cx="110" cy="40" r="225" stroke-width="6"/>
      <circle cx="110" cy="40" r="245" stroke-width="4"/>
      <circle cx="120" cy="60" r="270" stroke-width="3"/>
    </g>
    <g fill="none" stroke="#b9cc6a" opacity=".5">
      <circle cx="300" cy="40" r="90" stroke-width="6"/>
      <circle cx="300" cy="40" r="110" stroke-width="4"/>
      <circle cx="440" cy="90" r="70" stroke-width="5"/>
      <circle cx="300" cy="500" r="260" stroke-width="2"/>
      <circle cx="300" cy="500" r="245" stroke-width="1.5"/>
    </g>
    <circle cx="1200" cy="0" r="330" fill="url(#sun)" opacity=".9"/>
    <g fill="none" stroke="#e9b321" opacity=".7">
      <circle cx="1110" cy="40" r="200" stroke-width="6"/>
      <circle cx="1110" cy="40" r="225" stroke-width="4"/>
    </g>
    <g fill="none" stroke="#f3f4e2" opacity=".6">
      <circle cx="910" cy="300" r="300" stroke-width="10"/>
      <circle cx="910" cy="300" r="250" stroke-width="6"/>
      <circle cx="910" cy="300" r="200" stroke-width="4"/>
    </g>
    <g fill="none" stroke-width="3">
      <circle cx="306" cy="515" r="130" stroke="var(--orange)" opacity=".7"/>
      <circle cx="306" cy="515" r="122" stroke="var(--green)" opacity=".8"/>
      <circle cx="306" cy="515" r="140" stroke="var(--teal-soft)" opacity=".6"/>
    </g>
    <circle cx="306" cy="515" r="112" fill="url(#core-fill)"/>
    <g fill="none" stroke-width="1" opacity=".45">
      <circle cx="300" cy="328" r="66" stroke="var(--orange)"/>
      <circle cx="451" cy="437" r="66" stroke="var(--orange)"/>
      <circle cx="128" cy="437" r="66" stroke="var(--lime)"/>
      <circle cx="128" cy="605" r="66" stroke="var(--green)"/>
      <circle cx="451" cy="605" r="66" stroke="var(--teal-light)"/>
      <circle cx="300" cy="715" r="66" stroke="var(--teal)"/>
    </g>
    <circle cx="300" cy="328" r="54" fill="var(--orange)"/>
    <circle cx="451" cy="437" r="54" fill="var(--orange-light)"/>
    <circle cx="128" cy="437" r="54" fill="var(--lime)"/>
    <circle cx="128" cy="605" r="54" fill="var(--green)"/>
    <circle cx="451" cy="605" r="54" fill="var(--teal-light)"/>
    <circle cx="300" cy="715" r="54" fill="var(--teal-dark)"/>
    <g fill="none" stroke="var(--teal-dark)" opacity=".7">
      <circle cx="730" cy="601" r="100" stroke-width="3"/>
      <circle cx="735" cy="597" r="112" stroke-width="2"/>
      <circle cx="740" cy="593" r="124" stroke-width="1.5"/>
    </g>
    <circle cx="730" cy="601" r="89" fill="var(--teal-soft)"/>
    <circle cx="869" cy="570" r="40" fill="var(--teal-dark)"/>
    <circle cx="855" cy="686" r="40" fill="var(--teal)"/>
    <circle cx="748" cy="756" r="40" fill="var(--teal-light)"/>
    <g fill="var(--white)" font-family="Noto Serif, serif" font-size="46" text-anchor="middle">
      <text x="869" y="586">1</text>
      <text x="855" y="702">2</text>
      <text x="748" y="772">3</text>
    </g>
  </svg>

  <h1 class="display glance-title"><span class="big">mer-ova</span><span class="small">at a glance</span></h1>

  <p class="service-label center" style="left:200px;top:236px;width:200px;">Research and analysis<br>of cooperation schemes</p>
  <p class="service-label" style="left:53px;top:339px;">Facilitation of processes<br>of change</p>
  <p class="service-label right" style="right:653px;top:339px;">Training to improve<br>networked action</p>
  <p class="service-label" style="left:53px;top:683px;">Methodologies for<br>organizational change<br>and consensus building</p>
  <p class="service-label right" style="right:653px;top:683px;">Evaluation of<br>multi-actor projects<br>and programs</p>
  <p class="service-label center" style="left:200px;top:783px;width:200px;">Coalition building to achieve<br>collective goals</p>
  <p class="core-label">Analysis<br>of multi-actor<br>cooperation and<br>the facilitation<br>of processes of<br>change</p>

  <h2 class="display presence-title"><span class="big">our</span><span class="small">presence</span></h2>
  <div class="map" role="img" aria-label="World map of countries where Mer-ova has worked: North and South America highlighted in green, Europe in teal, North, East and Southern Africa in orange, Asia in gold, with dashed links between regions"></div>

  <h2 class="display projects-title"><span class="big">our</span><span class="small">projects</span></h2>
  <p class="project-text" style="left:924px;top:553px;">implementation of the Agenda 2030 and<br>the Sustainable Development Goals</p>
  <p class="project-text" style="left:912px;top:664px;">Organizational and technical development<br>of the Varnel Commission’s Policy<br>Forum on Development</p>
  <p class="project-text" style="left:799px;top:764px;">Networks of CSOs and Local Authorities from the Varnel Union and its<br>partner countries, as well as Varnel institutions</p>
</main>
</body>
</html>
```